Brennock Spa

We are a large Miami Beach spa and salon. I am still building our website but you can use it as a resource to gain a better understanding of who we are ....www.halvorwellness.example.

We offer a comprehensive list of services in hair, nails, massage, skin care, tanning, spray tanning and waxing and we offer high quality products for skin care, tanning and hair. We are open 7 days.

We would like to see a clean and simple menu that looks a lot like the one from "The Spa at Solvara." In particular, we have a copy of a menu from their West Hollywood, CA location that is just beautiful. In the uploaded content you will see a sampling of that menu. We would like to see greys, blacks, silvers, whites and warm colors like reds and oranges. We specifically attempt to remain gender neutral so that we don't attract only girls (with pink colors and flowers etc). The final design should convey a simple, clean, friendly environment and the final product should be sized such that it is 1.) portable and 2.) inexpensive to print. We will be running thousands of these at a time so cost of printing is a consideration.

The booklet consists of two parts: one part is the standard menu with descriptions of services and products and photos etc (think of this as the sales piece that convinces a potential customer to visit) and will be stapled together like you would expect a small menu to be and should resemble the Solvara menu. The prices should not be included in this part of the booklet that will be printed and stapled. The other part is a single insert and is removable and replaceable. I want this removable insert placed in the last page of the book in a folder pocket or something else that you can think of so that when it's time to change prices here that I am not throwing away all of the booklets....I am only replacing the inserts at the end of the menu booklet. Please design this single page insert so that should a customer remove it from the booklet and keep it, that it stands alone with our name, logo, website and phone number. This page can and probably will have to be 2 sided.

At the back of the booklet, I also want the polices to be printed in one page (think fine print in any sort of business dealing.)

With regard to the look and feel slider of economical v upmarket...we definitely want to convey we deliver upmarket services at reasonable prices. Think, world class services and products at reasonable, everyday prices.

With regard to the uploaded files:
I uploaded both EPS and TIF formats. The colors in those files are not the palette we want at all. The colors we want use for the circular logo must match the standard colors as depicted in the uploaded file "Brennocktanrooms"

Target Market(s)

The target market is the average 20-35 year old in Miami Beach that cares about their appearance. The range of clientele is quite diverse.

Industry/Entity Type

Environment

Requirements
Must have
• It must have elegant and simple photographs that relate to the services being offered. We are selling a service set and an environment...so this menu should be reflect that goal. The logo should be repeated often throughout the book but in subtle ways.

Stock photos are fine as long as they don't seem obviously stock.

Should not have
• Nothing buddha like. Nothing themed. It should be all inclusive and not seek to identify with any particular group or gender.

Nothing that fits the stereotype of "Miami Beach." We want to represent ourselves in the same category as the best spas in the world because we moving everything we do in that direction. Think class!

```html
<!DOCTYPE html>
<html lang="en">
<head>
<meta charset="utf-8">
<title>Brennock Spa – Service Menu Booklet</title>
<link rel="stylesheet" href="https://fonts.googleapis.com/css2?family=Open+Sans:wght@400;600;700&display=swap">
<style>
  :root{
    --canvas:#ffffff;
    --panel:#a3a2a2;
    --panel-text:#ffffff;
    --brand-black:#111111;
    --tag-hair:#8c8c8c;
    --tag-nails:#e48b1c;
    --tag-massage:#b4501e;
    --tag-skin:#c8202e;
    --tag-tanning:#a6b038;
    --tag-threading:#e0661b;
    --wood:#6b4a2e;
    --wood-dark:#3e2817;
    --fine-print:#f1e6d4;
    --price-black:#0e0e0e;
    --sheet:#ffffff;
    --sheet-edge:#e4e4e4;
  }
  *{box-sizing:border-box;margin:0;padding:0}
  html,body{width:787px;height:1200px;overflow:hidden;background:var(--canvas)}
  body{position:relative;font-family:"Open Sans",Arial,sans-serif}

  .page-single,.spread{position:absolute;overflow:hidden}
  .spread{width:355px;height:177px}
  .photo{position:absolute;left:0;top:0;bottom:0;width:229px}
  .fold{position:absolute;top:0;bottom:0;left:171px;width:16px;
        background:linear-gradient(90deg,rgba(255,255,255,0),rgba(255,255,255,.35),rgba(255,255,255,0))}
  .panel{position:absolute;left:229px;top:0;bottom:0;width:126px;background:var(--panel);
         color:var(--panel-text);padding:7px 6px 5px 7px}
  .panel h3{font-size:4.3px;font-weight:700;text-transform:uppercase;margin-top:3.4px;letter-spacing:.1px}
  .panel h3:first-child{margin-top:0}
  .panel p,.panel li{font-size:3.5px;line-height:1.4;font-weight:400}
  .panel ul{list-style:none}
  .continued{margin-top:4px;font-size:3.5px}

  .brand{position:absolute;left:2px;top:0;width:57px;height:39px;background:var(--brand-black);
         color:#fff;font-weight:600;text-align:center;display:flex;flex-direction:column;
         justify-content:center;align-items:center;font-size:5.2px;letter-spacing:.6px;line-height:1.5}
  .brand .sub{font-size:3.6px;letter-spacing:1.8px}
  .tag{position:absolute;left:2px;top:43px;width:57px;height:14px;color:#fff;font-weight:700;
       font-size:6.2px;line-height:1.15;text-transform:uppercase;display:flex;align-items:center;padding-left:5px}
  .tag.hair{background:var(--tag-hair)}
  .tag.nails{background:var(--tag-nails)}
  .tag.massage{background:var(--tag-massage)}
  .tag.skin{background:var(--tag-skin)}
  .tag.tanning{background:var(--tag-tanning);color:#1b1b1b}
  .tag.threading{background:var(--tag-threading);height:22px;font-size:6px}

  .cover{left:33px;top:28px;width:175px;height:179px}
  .cover .photo,.back-cover .photo{width:100%}
  .cover .brand{left:107px;top:17px;width:58px;height:60px;font-size:6px}
  .back-cover{left:581px;top:993px;width:177px;height:175px}

  .price-spread{left:33px;top:995px}
  .policies{position:absolute;left:0;top:0;width:177px;height:177px;
            background:linear-gradient(90deg,var(--wood-dark),var(--wood) 40%,#7a5535 60%,var(--wood-dark));
            color:var(--fine-print);padding:8px 8px}
  .policies p{font-size:3.4px;line-height:1.45;margin-bottom:3px}
  .policies strong{font-weight:700}
  .price-insert{position:absolute;left:177px;top:0;width:178px;height:177px;background:var(--wood-dark)}
  .price-insert svg{position:absolute;left:0;top:0}
  .price-title{position:absolute;left:18px;top:8px;z-index:1;font-size:7.5px;font-weight:700;
               color:var(--price-black);letter-spacing:.4px;line-height:1}
</style>
</head>
<body>

<section class="page-single cover">
  <div class="photo" role="img" aria-label="Stacked dark massage stones on a bamboo mat with green leaves and bamboo stalks before a wooden wall"
       style="background:linear-gradient(160deg,#4d7a2c 0%,#6b4a2e 35%,#2c1d12 65%,#7a3f2a 100%)"></div>
  <div class="brand"><span>BRENNOCK</span><span class="sub">SPA</span></div>
</section>

<section class="spread" style="left:407px;top:22px">
  <div class="photo" role="img" aria-label="Stylist combing and cutting long blonde hair"
       style="background:linear-gradient(120deg,#e8ddd0 0%,#c9a878 40%,#a88456 65%,#efe9e2 100%)"></div>
  <div class="fold"></div>
  <div class="brand"><span>BRENNOCK</span><span class="sub">SPA</span></div>
  <div class="tag hair">Hair</div>
  <div class="panel">
    <h3>Free Consultations</h3>
    <h3>Cutting</h3>
    <ul><li>Men's Cut</li><li>Women's Cut &amp; Style</li><li>Children's Cut</li></ul>
    <h3>Styling</h3>
    <ul><li>Blowout</li><li>Formal Updo</li><li>Bridal Trial</li><li>Wedding Day Style</li></ul>
    <h3>Coloring</h3>
    <ul><li>Single Process</li><li>Partial Highlights</li><li>Full Highlights</li><li>Color Gloss</li></ul>
    <h3>Treatments</h3>
    <ul><li>Deep Conditioning</li><li>Keratin Smoothing</li><li>Scalp Renewal</li></ul>
    <h3>Extensions</h3>
    <ul><li>Consultation</li><li>Application</li><li>Removal</li></ul>
  </div>
</section>

<section class="spread" style="left:33px;top:219px">
  <div class="photo" role="img" aria-label="Relaxed client lying on grass with hands raised showing painted nails"
       style="background:linear-gradient(180deg,#5f9a3a 0%,#7fae4c 35%,#d9b59a 60%,#4c7d2b 100%)"></div>
  <div class="fold"></div>
  <div class="brand"><span>BRENNOCK</span><span class="sub">SPA</span></div>
  <div class="tag nails">Nails</div>
  <div class="panel">
    <h3>Basic Nail Polishing</h3>
    <p>A quick shape and polish for hands or feet, finished with a glossy coat of your chosen colour.</p>
    <h3>The Express</h3>
    <p>Nails are trimmed, filed and buffed, cuticles tidied and a relaxing massage precedes a fresh polish.</p>
    <h3>The Classic</h3>
    <p>Our signature service adds a warm soak, gentle exfoliation and extended massage before polish is applied with care.</p>
    <h3>Delish</h3>
    <p>A rich sugar scrub and warm mask leave skin soft and smooth while you unwind in comfort.</p>
    <p class="continued">Continued &gt;</p>
  </div>
</section>

<section class="spread" style="left:407px;top:219px">
  <div class="photo" role="img" aria-label="Manicurist applying red polish to a client's nails"
       style="background:linear-gradient(135deg,#f2efec 0%,#e3c9b8 40%,#c99d86 60%,#f5f3f1 100%)"></div>
  <div class="fold"></div>
  <div class="brand"><span>BRENNOCK</span><span class="sub">SPA</span></div>
  <div class="tag nails">Nails</div>
  <div class="panel">
    <h3>The Ultimate</h3>
    <p>Our most complete treatment pairs a paraffin dip, hydrating mask and hot stone massage with flawless polish.</p>
    <ul><li>Ultimate Manicure</li><li>Ultimate Pedicure</li><li>Ultimate Combination</li></ul>
    <h3>Natural Nail Overlays</h3>
    <p>Strength and shine layered over natural nails without added length.</p>
    <ul><li>Gel Overlay</li><li>Gel Polish</li><li>Fill</li><li>Removal</li></ul>
    <h3>Additional Charges</h3>
    <ul><li>Nail Art</li><li>French Finish</li><li>Paraffin Dip</li><li>Polish Change</li></ul>
  </div>
</section>

<section class="spread" style="left:33px;top:416px">
  <div class="photo" role="img" aria-label="Therapist giving a back massage to a client lying beside a tray of spa accessories"
       style="background:linear-gradient(110deg,#f4ece2 0%,#d9a77e 35%,#b97a52 60%,#e9dfd3 100%)"></div>
  <div class="fold"></div>
  <div class="brand"><span>BRENNOCK</span><span class="sub">SPA</span></div>
  <div class="tag massage">Massage</div>
  <div class="panel">
    <h3>Swedish Massage</h3>
    <p>Long flowing strokes ease tension, improve circulation and bring the whole body into deep relaxation.</p>
    <h3>Aromatherapy</h3>
    <p>Pure essential oils are chosen to calm or energize, blended into a soothing full body massage.</p>
    <h3>Deep Tissue Massage</h3>
    <p>Firm, focused pressure reaches deeper muscle layers to release chronic knots and restore ease of movement.</p>
    <h3>Hot Stone Therapy</h3>
    <p>Smooth heated stones glide over the body, warming muscles so tension melts away with less effort.</p>
    <h3>Prenatal Massage</h3>
    <p>Gentle, supported positioning and careful technique relieve the aches of pregnancy for mother and baby.</p>
    <p class="continued">Continued &gt;</p>
  </div>
</section>

<section class="spread" style="left:407px;top:416px">
  <div class="photo" role="img" aria-label="Client lying face down receiving a shoulder massage"
       style="background:linear-gradient(120deg,#f7f4f0 0%,#dcc3ac 40%,#c49a78 60%,#f4f1ed 100%)"></div>
  <div class="fold"></div>
  <div class="brand"><span>BRENNOCK</span><span class="sub">SPA</span></div>
  <div class="tag massage">Massage</div>
  <div class="panel">
    <h3>Sports-Specific Massage</h3>
    <p>Designed for active clients, this session combines stretching and targeted work to aid recovery and prevent injury before or after training.</p>
    <h3>Prenatal Massage</h3>
    <p>Offered after the first trimester, this nurturing treatment reduces swelling and supports restful sleep.</p>
    <h3>Reflexology</h3>
    <p>Pressure applied to points on the feet and hands encourages balance throughout the body and a calm mind.</p>
  </div>
</section>

<section class="spread" style="left:33px;top:612px">
  <div class="photo" role="img" aria-label="Client resting on a white towel receiving a head massage"
       style="background:linear-gradient(120deg,#f3ede6 0%,#caa27e 35%,#8a5b3a 55%,#f2ede8 100%)"></div>
  <div class="fold"></div>
  <div class="brand"><span>BRENNOCK</span><span class="sub">SPA</span></div>
  <div class="tag massage">Massage</div>
  <div class="panel">
    <h3>Shiatsu</h3>
    <p>A traditional technique using rhythmic finger pressure along energy lines, performed fully clothed on a padded mat to restore balance and vitality.</p>
    <h3>Thai Massage</h3>
    <p>Assisted stretches and compression improve flexibility and release tension, leaving you energized and light on your feet.</p>
  </div>
</section>

<section class="spread" style="left:407px;top:612px">
  <div class="photo" role="img" aria-label="Client with hair wrapped in a towel receiving a facial"
       style="background:linear-gradient(120deg,#6b3f22 0%,#d8b59a 35%,#efe4da 60%,#f7f5f2 100%)"></div>
  <div class="fold"></div>
  <div class="brand"><span>BRENNOCK</span><span class="sub">SPA</span></div>
  <div class="tag skin">Skin Care</div>
  <div class="panel">
    <h3>Clinical Facial</h3>
    <p>A results driven facial tailored to your skin, with deep cleansing, extractions and targeted serums.</p>
    <ul><li>The 60 Minute Clinical Facial</li><li>The 90 Minute Clinical Facial</li></ul>
    <h3>Organic Facial</h3>
    <p>Plant based products nourish and brighten skin in a calming, purely natural treatment.</p>
    <ul><li>The 60 Minute Organic Facial</li><li>The 90 Minute Organic Facial</li></ul>
    <h3>Chemical Peel</h3>
    <p>A gentle peel lifts dull surface cells to reveal a smoother, more even and radiant complexion.</p>
    <h3>Microdermabrasion</h3>
    <p>Fine exfoliation refines texture, softens fine lines and clears congested pores with no downtime.</p>
  </div>
</section>

<section class="spread" style="left:33px;top:808px">
  <div class="photo" role="img" aria-label="Client lying in a glowing blue tanning bed"
       style="background:linear-gradient(180deg,#050a30 0%,#1a3fb8 40%,#6fa0ff 55%,#0b1650 100%)"></div>
  <div class="fold"></div>
  <div class="brand"><span>BRENNOCK</span><span class="sub">SPA</span></div>
  <div class="tag tanning">Tanning</div>
  <div class="panel">
    <h3>UV Tanning</h3>
    <p>Our modern beds offer a range of intensities for a deep, even tan in minutes.</p>
    <h3>Unlimited UV Memberships</h3>
    <p>Tan as often as you like with one simple monthly rate.</p>
    <h3>UV Series</h3>
    <p>Save with bundled sessions valid for six months.</p>
    <h3>UV Sessions</h3>
    <ul><li>Single Session</li><li>Five Sessions</li><li>Ten Sessions</li></ul>
    <h3>Custom Airbrush Tanning</h3>
    <p>A certified artist applies a natural looking, streak free tan tailored to your skin tone.</p>
  </div>
</section>

<section class="spread" style="left:407px;top:808px">
  <div class="photo" role="img" aria-label="Aesthetician applying a wax strip to a client's leg"
       style="background:linear-gradient(120deg,#f4eee8 0%,#e0bfa2 40%,#c89a76 60%,#f6f3ef 100%)"></div>
  <div class="fold"></div>
  <div class="brand"><span>BRENNOCK</span><span class="sub">SPA</span></div>
  <div class="tag threading">Threading<br>&amp; Waxing</div>
  <div class="panel">
    <h3>Threading</h3>
    <p>An ancient method using twisted cotton thread to shape brows and remove fine facial hair with precision, gentle on even sensitive skin.</p>
    <h3>Waxing</h3>
    <p>Warm wax removes hair from the root for smooth results that last for weeks, using formulas chosen for comfort and care.</p>
  </div>
</section>

<section class="spread price-spread">
  <div class="policies">
    <p><strong>Arrival:</strong> Please arrive fifteen minutes early so your treatment can begin on time.</p>
    <p><strong>Cancellations:</strong> We ask for twenty four hours notice to cancel or change any appointment.</p>
    <p><strong>Late Arrivals:</strong> Late arrivals may receive a shortened service at the full price.</p>
    <p><strong>Gift Cards:</strong> Gift cards are non refundable and may be used toward any service.</p>
    <p><strong>Gratuity:</strong> Gratuity is at your discretion and may be left for your provider.</p>
    <p><strong>Health:</strong> Please tell us of any medical conditions or allergies before your service.</p>
  </div>
  <div class="price-insert">
    <svg width="178" height="177" viewBox="0 0 178 177" aria-hidden="true">
      <rect x="0" y="0" width="178" height="177" fill="#4a3220"/>
      <polygon points="10,4 176,4 176,150 10,177" fill="#ffffff"/>
      <polygon points="44,22 172,22 172,92 44,116" fill="#f3f3f3" stroke="#e4e4e4" stroke-width="1"/>
      <polygon points="10,177 176,70 176,177" fill="#0e0e0e"/>
    </svg>
    <div class="price-title">PRICE LIST</div>
  </div>
</section>

<section class="page-single back-cover">
  <div class="photo" role="img" aria-label="White orchid with dark massage stones, green leaves and bamboo on a wooden surface"
       style="background:linear-gradient(160deg,#5a3a22 0%,#7c5434 40%,#4f7d2c 60%,#8a3c2a 100%)"></div>
</section>

</body>
</html>
```